New York Property Management Company needs a Brochure Designed

We need a brochure for a new property management company in New York called KT7 Realty Partners. The 2 is superscript (squared.) We are looking for buildings to manage and want to showcase our expertise and caring. Logo is attached. We are getting a different photo and do not need all the verbiage. Also, does not need to be a trifold.
Updates

Property management group is a RESIDENTIAL property management group. I neglected to mention that. Thanks.

Reason: A few people have to weigh in on the design and it has been difficult coordinating this. We are getting close to making a decision and just need a few more days.

Industry/Entity Type

Property Management

```html
<!DOCTYPE html>
<html lang="en">
<head>
<meta charset="utf-8">
<title>KT7 Realty Partners – Founders</title>
<link href="https://fonts.googleapis.com/css2?family=Open+Sans:wght@800&family=Didact+Gothic&display=swap" rel="stylesheet">
<style>
  :root {
    --page: #e9e7e5;
    --header-dark: #2e2a29;
    --header-mid: #4a4443;
    --panel: #5b5655;
    --panel-text: #e8e4e1;
    --name-text: #ffffff;
    --badge: #8e8a88;
    --badge-text: #f2f0ee;
    --photo-dark: #1f1c1c;
    --photo-mid: #5e5857;
  }
  * { box-sizing: border-box; margin: 0; padding: 0; }
  html, body { width: 1200px; height: 600px; overflow: hidden; background: var(--page); }
  .brochure { position: relative; width: 1200px; height: 600px; font-family: "Didact Gothic", sans-serif; }

  .header {
    position: absolute; top: 0; height: 92px;
    background: linear-gradient(180deg, var(--header-mid) 0%, var(--header-dark) 100%);
  }
  .header--left { left: 0; width: 600px; }
  .header--right { left: 602px; width: 598px; }
  .founder-name {
    position: absolute; top: 20px;
    font-family: "Open Sans", sans-serif; font-weight: 800;
    font-size: 37px; letter-spacing: 0.5px; color: var(--name-text);
    text-transform: uppercase; line-height: 1;
  }
  .header--left .founder-name { left: 18px; }
  .header--right .founder-name { left: 32px; }

  .brand-badge {
    position: absolute; top: 0; width: 60px; height: 89px;
    background: var(--badge);
    display: flex; align-items: center; justify-content: center; text-align: center;
    font-family: "Didact Gothic", sans-serif; font-size: 11px; line-height: 1.25;
    color: var(--badge-text); padding: 4px;
  }
  .header--left .brand-badge { left: 511px; }
  .header--right .brand-badge { left: 509px; }

  .bio-panel {
    position: absolute; top: 92px; height: 508px;
    background: var(--panel); color: var(--panel-text);
    font-size: 12px; line-height: 14.2px;
  }
  .bio-panel--left { left: 0; width: 422px; padding: 50px 22px 0 42px; }
  .bio-panel--right { left: 770px; width: 430px; padding: 54px 22px 0 27px; }
  .bio-panel p + p { margin-top: 14px; }

  .founders-photo {
    position: absolute; left: 434px; top: 92px; width: 324px; height: 508px;
    background: linear-gradient(180deg, var(--photo-mid) 0%, #3b3636 30%, var(--photo-dark) 70%, #4d4746 100%);
  }
</style>
</head>
<body>
<main class="brochure">
  <header class="header header--left">
    <h1 class="founder-name">Marcus Linwood</h1>
    <div class="brand-badge">KT7 Realty Partners</div>
  </header>
  <header class="header header--right">
    <h1 class="founder-name">Dana Ferraro</h1>
    <div class="brand-badge">KT7 Realty Partners</div>
  </header>

  <section class="bio-panel bio-panel--left">
    <p>Prior to co-founding KT7 Realty Partners, Marcus was the Acquisitions Manager and a Senior Property Manager at Harborline Residential New York, LLC (formerly Bleecker Row Realty, Inc.) managing properties and locating investment opportunities for the principals of Harborline. Marcus used his management, investment and development knowledge to create and implement asset repositioning plans including renovations and re-leasing for investments in order to maximize value for investors. Marcus has managed over 1200 units in more than 30 buildings including residential and commercial owners/tenants and 50+ staff members.</p>
    <p>Marcus has experience in high end and affordable housing including rent stabilized units in the rental, coop and condo markets both from Harborline and his prior position at The Ashgrove Group in Washington, DC. He began working in property management upon graduation from Chesapeake State University with a degree in Economics. Marcus grew up in Minneapolis, MN.</p>
    <p>Marcus established himself as a leading manager and key investment advisor at Harborline. He is an entrepreneur and is parlaying his unique skills and knowledge into making KT7 one of New York City's leading property management and real estate investment firms.</p>
  </section>

  <div class="founders-photo" role="img" aria-label="Photo of the two founders standing together on a city rooftop with apartment buildings behind them"></div>

  <section class="bio-panel bio-panel--right">
    <p>Before co-founding KT7 Realty Partners, Dana was a Team Leader at Harborline Residential (formerly Bleecker Row), managing a team of 10+ managers responsible for a portfolio of multi-family building varying in size, location and prominence in Manhattan, Riverdale and Queens. She has been in property management for 12 years. She also served as Vice President of Client Accounting, utilizing her accounting background and management experience to restructure the department to better serve Bleecker Row clients.</p>
    <p>Dana has over 20 years of experience in various aspects of the management business. She was Board President of a large Westside Manhattan cooperative for more than 10 years. She began her career in New York at Meridian Financial in finance, accounting and marketing positions. Her passion and interest in the management business prompted her to change careers and she joined a small management company in 2002. She rose through the ranks to both lead Client Accounting and her management team.</p>
    <p>During Dana's tenure at Harborline/Bleecker Row, she established herself as a high performing manager and leader. Her broad scope of experience and education continue to be utilized by many buildings in improving financial performance, building operations and staff management. She is continuing to leverage these skills in building KT7RP.</p>
  </section>
</main>
</body>
</html>
```